we can communicate on this, but i want to follow the approach we took on Pellow|Quint & Marsh but i feel the card front needs the black background and the platinum and gold logo. The back? I am open. we can use the same info from PQ&M. Velmora Point is an enhanced equity investment fund - basically a very exclusive boutique hedge fund that uses only stock options. very advanced things. hope you are interested

Contact Information for Business Card

Dr. Lewis T. Brennick, CFA
Scientifique de fusée financière
701.555.0143
LBdoc4490@mailvex.example

4817 Birch Hollow Way W.
West Fargo, ND 58099

No web site

Colors

Designer to choose colors to be used in the design.

Requirements
Nice to have
• I tend to prefer the most visible applications of the logo to include logo and name, the logo version with a black background and the gold and platinum components separated by the black. I see this working well for a single side (logo and name - this is card front to me).
• I am fairly open to other treatments on the reverse side with the data. To me, it makes sense to have a different color rendition of the logo on the reverse and it may be a muted black tone on tone or an oversized portion that would have spot UV. Or, the reverse may play with colors and layout
Should not have
• Other colors = no no
• Decorative font

```html
<!DOCTYPE html>
<html lang="en">
<head>
<meta charset="utf-8">
<title>Velmora Point – Business Card</title>
<link rel="stylesheet" href="https://fonts.googleapis.com/css2?family=Roboto:ital,wght@0,400;0,700;1,400&display=swap">
<style>
  :root {
    --backdrop: #1f1f20;
    --card-black: #1a1b1d;
    --seal-black: #030303;
    --gold-light: #e4cf72;
    --gold-mid: #d8b946;
    --gold-deep: #cfae3c;
    --platinum: #c9c9cc;
    --ring: #b8b3b8;
    --white: #ffffff;
  }
  * { box-sizing: border-box; margin: 0; padding: 0; }
  html, body {
    width: 1200px; height: 800px; overflow: hidden;
    background: var(--backdrop);
    font-family: "Roboto", Arial, sans-serif;
  }
  .canvas { position: relative; width: 1200px; height: 800px; }
  .card {
    position: absolute; width: 500px; height: 286px;
    overflow: hidden;
    box-shadow: 0 10px 30px rgba(0,0,0,.45);
  }
  /* Front */
  .card-front {
    left: 70px; top: 257px;
    background: var(--card-black);
    display: flex; flex-direction: column; align-items: center; justify-content: center;
  }
  .brand-mark {
    width: 92px; height: 92px; border-radius: 50%;
    background: #5a5a5d;
    margin-bottom: 18px;
  }
  .brand-name {
    color: var(--platinum);
    font-weight: 700; font-size: 30px; letter-spacing: 3px;
    text-transform: uppercase; line-height: 1.1; text-align: center;
  }
  /* Back */
  .card-back {
    left: 630px; top: 257px;
    background: linear-gradient(200deg, var(--gold-deep) 0%, var(--gold-mid) 45%, var(--gold-light) 100%);
  }
  .seal {
    position: absolute; left: 230px; top: -40px;
    width: 370px; height: 370px; border-radius: 50%;
    background: var(--seal-black);
    border: 5px solid var(--ring);
  }
  .seal-brand {
    position: absolute; left: 300px; top: 62px; width: 190px;
    display: flex; flex-direction: column; align-items: center;
  }
  .seal-brand .brand-mark {
    width: 72px; height: 72px; margin-bottom: 14px;
    background: var(--gold-mid);
  }
  .seal-brand .brand-name {
    color: var(--white); font-size: 24px; letter-spacing: 2px;
  }
  .contact {
    position: absolute; left: 26px; top: 92px; width: 210px;
    color: var(--white);
  }
  .contact-name { font-size: 17px; font-weight: 700; white-space: nowrap; }
  .contact-name .credential { font-size: 11px; font-weight: 400; vertical-align: 4px; }
  .contact-title { font-size: 11.5px; font-style: italic; margin-bottom: 12px; white-space: nowrap; }
  .contact-block { font-size: 12px; line-height: 1.35; margin-bottom: 12px; white-space: nowrap; }
</style>
</head>
<body>
<main class="canvas">
  <section class="card card-front" aria-label="Card front">
    <div class="brand-mark"></div>
    <div class="brand-name">Velmora<br>Point</div>
  </section>

  <section class="card card-back" aria-label="Card back">
    <div class="seal"></div>
    <div class="seal-brand">
      <div class="brand-mark"></div>
      <div class="brand-name">Velmora<br>Point</div>
    </div>
    <div class="contact">
      <p class="contact-name">Dr. Lewis T. Brennick, <span class="credential">CFA</span></p>
      <p class="contact-title">Scientifique des Fusées Financières</p>
      <p class="contact-block">4817 Birch Hollow Way W.<br>West Fargo, ND 58099</p>
      <p class="contact-block">P. 701.555.0143<br>LBdoc4490@mailvex.example</p>
    </div>
  </section>
</main>
</body>
</html>
```